Restaurant Finder Website Design

I need to create a website that will help people find restaurants around a zip code or address.

I would like to have a very clean and simple design. I will need a design for the homepage, that should be very clean and simple to use. its where the users will launch their search. I am thinking something like tavlex like.. big search field with a very clean page where users can create an account or restaurants subscribe to the service.

Also need the design of the search results page, I would like to display a big map with the results and a list on the side or the bottom of the map.

Also need a profile page for the users that sign up to the site.

Mostly what I need are guidelines and color coordinated elements, like a general layout and buttons that work together. I would like to know what the action buttons and elements should look like. Because its going to have some more detail pages.

Target Market(s)

People in general, mainly people that work at an office and have to find a place for lunch every day.

Industry/Entity Type

Restaurant

Number of Pages Required

4 page

Font styles to use
Serif
Sans Serif

Requirements
Must have
• It must be a really simple and clean design but look edgy.

```html
<!DOCTYPE html>
<html lang="en">
<head>
<meta charset="utf-8">
<title>ForkNear — Find restaurants near you</title>
<link rel="stylesheet" href="https://fonts.googleapis.com/css2?family=Open+Sans:wght@400;600&family=Questrial&display=swap">
<style>
  :root {
    --brand-red: #c61f26;
    --icon-pink: #f07a7e;
    --ink-dark: #363840;
    --text-muted: #777777;
    --text-footer: #222222;
    --bar-bg: #f5f5f5;
    --bar-border: #e2e2e2;
    --button-grey: #666666;
    --button-black: #050505;
    --white: #ffffff;
    --placeholder: #9a9a9a;
  }
  * { box-sizing: border-box; margin: 0; padding: 0; }
  html, body { width: 1200px; height: 709px; overflow: hidden; background: var(--white); }
  body { position: relative; font-family: "Open Sans", Arial, sans-serif; }

  .top-bar {
    position: absolute; left: 0; top: 0; width: 1200px; height: 59px;
    background: var(--bar-bg); border-bottom: 1px solid var(--bar-border);
  }
  .top-bar__tagline {
    position: absolute; left: 60px; top: 22px;
    font-size: 13px; color: var(--text-muted);
  }
  .account-button {
    position: absolute; top: 10px; width: 79px; height: 37px;
    background: var(--button-grey); color: var(--white); border-radius: 3px;
    font-family: "Questrial", Arial, sans-serif; font-size: 18px;
    display: flex; align-items: center; justify-content: center;
  }
  .account-button--login { left: 975px; }
  .account-button--signup { left: 1060px; }

  .brand {
    position: absolute; left: 0; top: 205px; width: 1200px;
    display: flex; align-items: center; justify-content: center; gap: 18px;
  }
  .brand__dot { width: 72px; height: 72px; border-radius: 50%; background: var(--brand-red); }
  .brand__name {
    font-family: "Questrial", Arial, sans-serif; font-size: 46px; color: var(--ink-dark);
  }

  .search-panel {
    position: absolute; left: 172px; top: 347px; width: 874px; height: 126px;
    background: var(--brand-red); border-radius: 4px;
  }
  .search-panel__icon { position: absolute; left: 18px; top: 46px; }
  .search-panel__heading {
    position: absolute; left: 83px; top: 16px;
    font-family: "Questrial", Arial, sans-serif; font-size: 17px; color: var(--white);
  }
  .search-field {
    position: absolute; top: 55px; height: 46px; background: var(--white); border-radius: 3px;
    display: flex; align-items: center; gap: 8px; padding-left: 10px;
    font-size: 15px; color: var(--placeholder);
  }
  .search-field--zip { left: 85px; width: 221px; }
  .search-field--address { left: 354px; width: 366px; padding-left: 12px; }
  .search-panel__or {
    position: absolute; left: 322px; top: 67px;
    font-family: "Questrial", Arial, sans-serif; font-size: 17px; color: var(--white);
  }
  .search-button {
    position: absolute; left: 734px; top: 55px; width: 123px; height: 46px;
    background: var(--button-black); color: var(--white); border-radius: 2px;
    font-family: "Questrial", Arial, sans-serif; font-size: 21px;
    display: flex; align-items: center; justify-content: center;
  }

  .site-footer {
    position: absolute; left: 0; top: 648px; width: 1200px; height: 61px;
    background: var(--bar-bg); border-top: 1px solid var(--bar-border);
    display: flex; align-items: center; justify-content: center;
    font-size: 13.5px; color: var(--text-footer);
  }
</style>
</head>
<body>
  <header class="top-bar">
    <p class="top-bar__tagline">We help people find restaurants using zip code or address.</p>
    <a class="account-button account-button--login">Login</a>
    <a class="account-button account-button--signup">Signup</a>
  </header>

  <main>
    <div class="brand">
      <span class="brand__dot"></span>
      <span class="brand__name">ForkNear</span>
    </div>

    <section class="search-panel">
      <svg class="search-panel__icon" width="54" height="56" viewBox="0 0 54 56" aria-hidden="true">
        <circle cx="21" cy="21" r="17" fill="none" stroke="var(--icon-pink)" stroke-width="4.5"/>
        <path d="M10 17 a11 11 0 0 1 5 -8" fill="none" stroke="var(--icon-pink)" stroke-width="2.5" stroke-linecap="round"/>
        <line x1="34" y1="34" x2="48" y2="49" stroke="var(--icon-pink)" stroke-width="7" stroke-linecap="round"/>
      </svg>
      <h1 class="search-panel__heading">We help people find restaurants around a zip code or address.</h1>

      <div class="search-field search-field--zip">
        <svg width="14" height="20" viewBox="0 0 14 20" aria-hidden="true">
          <path d="M7 0 A7 7 0 0 0 0 7 C0 12 7 20 7 20 C7 20 14 12 14 7 A7 7 0 0 0 7 0 Z M7 4.5 A2.5 2.5 0 1 1 7 9.5 A2.5 2.5 0 1 1 7 4.5 Z" fill="var(--placeholder)" fill-rule="evenodd"/>
        </svg>
        <span>Enter Zip Code</span>
      </div>
      <span class="search-panel__or">or</span>
      <div class="search-field search-field--address">
        <svg width="20" height="20" viewBox="0 0 20 20" aria-hidden="true">
          <path d="M20 0 L0 8.5 L9 11 L11.5 20 Z" fill="var(--placeholder)"/>
        </svg>
        <span>Enter Address</span>
      </div>
      <a class="search-button">Search</a>
    </section>
  </main>

  <footer class="site-footer">© 2016 Copyright Fork Near All Rights Reserved</footer>
</body>
</html>
```